Bref créative
Marketing Materials For Brightwater Home Renovations, LLC
Need brochure, postcards, Thank you/referral cards, Truck sign, T-shirt
Long Island Home Remodeling & Design
Looking for a brochure design for racks. A thank you note that can also serve as a referral card. I will post the referral content in the comment section. The truck sign will be a magnet approx. 24" x 24". Flexible with the t-shirt.
Construction
I'm looking for professional as well as heartfelt. We are a home remodeling and design company focused on customer service, quality, value and creativity. Target audience is people looking for more than a faceless general contractor to remodel their home. We are striving to be a home improvement company with personality and enthusiasm.
not sure besides basic info. You can take a look at our website in progress for ideas of who we are and aim to be. Brightwaterhomerenovations.example As long as I can edit the content in the end, I'm ok with you putting in filler for now.
Brightwater Home Renovations, LLC Logo
Mug Shot
Some Literature
referral content

```html
<!DOCTYPE html>
<html lang="en">
<head>
<meta charset="utf-8">
<title>Brightwater Home Renovations – Brochure</title>
<link href="https://fonts.googleapis.com/css2?family=Open+Sans:wght@400;600;700&family=Oswald:wght@500;700&display=swap" rel="stylesheet">
<style>
:root{
  --navy:#1b3a5c;
  --blue:#2f7fc1;
  --sky:#8fc3e8;
  --pale:#e4f0f9;
  --ink:#444b52;
  --muted:#7a848c;
  --paper:#ffffff;
  --stage:#e9ebee;
}
*{box-sizing:border-box;margin:0;padding:0}
html,body{width:1200px;height:1004px;overflow:hidden;background:var(--stage)}
body{font-family:"Open Sans",Arial,sans-serif;color:var(--ink);position:relative}
.sheet{position:absolute;left:290px;width:620px;height:480px;background:var(--paper);display:flex;box-shadow:0 2px 8px rgba(0,0,0,.18)}
.sheet--outside{top:15px}
.sheet--inside{top:509px;flex-direction:column}
.panel{width:206.6px;height:100%;position:relative;padding:10px 11px;font-size:6.4px;line-height:1.45}
.panel+.panel{border-left:1px solid #eef1f4}
.heading{display:block;background:var(--navy);color:#fff;font:600 8px "Open Sans",sans-serif;padding:3px 6px;margin:0 -11px 7px -11px;width:62%;clip-path:polygon(0 0,100% 0,88% 100%,0 100%)}
p{margin-bottom:5px}
.photo{background:linear-gradient(135deg,#b8c3cc,#6f7d88)}
.owner{display:flex;gap:7px;margin-bottom:6px}
.owner .photo{width:54px;height:66px;flex:none;background:linear-gradient(160deg,#d9c2a8,#7b6553)}
.brand{display:flex;align-items:center;gap:6px;justify-content:center}
.brand-mark{width:18px;height:18px;background:var(--navy);flex:none}
.brand-name{font:700 11px "Oswald",sans-serif;color:var(--navy);text-transform:uppercase;line-height:1.05}
.tagline{text-align:center;font-size:6.4px;color:var(--navy);font-weight:600;margin-top:3px}
.contact{text-align:center;margin-top:8px}
.contact .name{font-weight:700;font-size:7.5px;color:var(--navy)}
.contact .phone{font:700 18px "Oswald",sans-serif;color:var(--blue);line-height:1.2}
.blueprint{background:linear-gradient(160deg,var(--pale),var(--sky) 60%,var(--blue))}
.return{position:absolute;left:0;right:0;bottom:0;height:62px;background:var(--navy);color:#fff;text-align:center;padding-top:14px;font-size:6.6px}
.cover{padding:0}
.cover .photo{height:150px;background:linear-gradient(135deg,#c9d6e2,#7d93a8)}
.cover .band{padding:12px 8px 8px}
.cover .brand-name{font-size:14px}
.cover .blueprint{position:absolute;left:0;right:0;bottom:0;height:248px}
.inside-top{display:flex;height:368px}
.photos{display:flex;gap:4px;margin:0 0 8px}
.photos .photo{flex:1;height:70px}
.photos .p1{background:linear-gradient(135deg,#cfc6b3,#8a7f6d)}
.photos .p2{background:linear-gradient(135deg,#9fb19a,#5b6b5a)}
.photos .p3{background:linear-gradient(135deg,#b79476,#5e4634)}
.wide{display:flex;flex-direction:column;width:413.2px}
.wide .cols{display:flex;gap:14px}
.wide .cols > div{flex:1}
.sub{font-weight:700;color:var(--navy);display:block}
.services{display:grid;grid-template-columns:1fr 1fr;gap:3px 8px;margin-top:4px}
.services li{list-style:none;font-size:6.6px;font-weight:600;color:var(--navy);padding-left:9px;position:relative}
.services li::before{content:"";position:absolute;left:0;top:2px;width:5px;height:5px;background:var(--blue)}
.tools{height:70px;margin-top:12px;background:linear-gradient(135deg,#e8d9a8,#9aa6b0)}
.inside-bottom{display:flex;height:112px}
.start{width:413.2px;background:linear-gradient(90deg,var(--navy),var(--blue));color:#fff;padding:9px 12px;position:relative}
.start h3{font:700 8px "Open Sans",sans-serif}
.start h2{font:700 17px "Oswald",sans-serif;letter-spacing:.5px;margin-bottom:6px}
.steps{display:flex;gap:10px;width:62%}
.step{flex:1;font-size:6px;line-height:1.4}
.step b{display:block;font:700 13px "Oswald",sans-serif}
.start .photo{position:absolute;right:12px;top:14px;width:130px;height:84px;background:linear-gradient(135deg,#f0e6c4,#8a99a6)}
.closing{width:206.8px;padding:10px 11px;font-size:6.4px;line-height:1.45;position:relative}
.closing .brand{position:absolute;right:12px;bottom:10px}
</style>
</head>
<body>

<section class="sheet sheet--outside" aria-label="Brochure outside">
  <div class="panel">
    <span class="heading">Meet The Owner</span>
    <div class="owner">
      <div class="photo" role="img" aria-label="Portrait of the owner"></div>
      <p>Hello, my name is Daniel. I started this company because I believe every home deserves honest work, careful planning and a builder who truly listens to the family living there.</p>
    </div>
    <p>From the first visit to the final walkthrough, I personally make sure every project is finished with pride. We treat your home as if it were our own, keep you informed at each step and leave every room cleaner than we found it.</p>
    <span class="heading">About Us</span>
    <p>Brightwater Home Renovations is a Long Island remodeling and design company built on customer service, quality, value and creativity. We are more than a faceless general contractor.</p>
    <p>Our team brings personality and enthusiasm to kitchens, baths, basements and additions. We help you shape ideas into plans, choose materials that fit your budget and enjoy a smooth, well organised build.</p>
    <p>Whether you need a small repair or a complete transformation, we are ready to help you love where you live.</p>
  </div>

  <div class="panel">
    <div class="brand" style="margin-top:14px">
      <span class="brand-mark"></span>
      <span class="brand-name">Brightwater</span>
    </div>
    <div class="contact">
      <div class="name">Daniel P. Marsh</div>
      <div>Call for a FREE Estimate</div>
      <div class="phone">631-555-0148</div>
      <div>Brightwaterhomerenovations.example</div>
    </div>
    <div class="blueprint" role="img" aria-label="Blueprint drawing" style="height:210px;margin:12px -11px 0"></div>
    <div class="return">11 Harbor Lane<br>Anytown, NY 11700<br>Brightwaterhomerenovations.example</div>
  </div>

  <div class="panel cover">
    <div class="photo" role="img" aria-label="Handshake over building plans"></div>
    <div class="band">
      <div class="brand"><span class="brand-mark"></span><span class="brand-name">Brightwater<br>Home Renovations</span></div>
      <div class="tagline">Long Island Home Remodeling &amp; Design</div>
    </div>
    <div class="blueprint" role="img" aria-label="Blueprint drawing"></div>
  </div>
</section>

<section class="sheet sheet--inside" aria-label="Brochure inside">
  <div class="inside-top">
    <div class="panel">
      <span class="heading">Our Process</span>
      <span class="sub">FREE Estimate and In-Home Consultation</span>
      <p>We meet you at home, listen to your goals and walk through the space together so nothing is missed.</p>
      <span class="sub">Design</span>
      <p>Our designers turn your ideas into clear drawings, material choices and a plan that respects your budget and timeline.</p>
      <span class="sub">Build</span>
      <p>Skilled crews arrive on time, protect your home and keep the site tidy every day while the work moves forward.</p>
      <span class="sub">Inspect</span>
      <p>We check every detail with you and fix anything that is not exactly right before calling the job complete.</p>
      <span class="sub">Complete</span>
      <p>You enjoy your new space, backed by our workmanship warranty.</p>
    </div>
    <div class="panel wide">
      <div class="photos">
        <div class="photo p1" role="img" aria-label="Finished home exterior"></div>
        <div class="photo p2" role="img" aria-label="Renovated house front"></div>
        <div class="photo p3" role="img" aria-label="Remodeled kitchen"></div>
      </div>
      <div class="cols">
        <div><p>Every project starts with a conversation. We want to know how you live, what you love and what frustrates you about your current space. That is how we design rooms that feel personal and work well.</p><p>We plan carefully, price honestly and keep you updated so you always know what happens next.</p></div>
        <div><p>Our crews take pride in clean lines, solid framing and finishes that last. We choose trusted suppliers and stand behind each job long after the last nail is set.</p><p>Ask about our referral rewards and seasonal offers.</p></div>
      </div>
    </div>
    <div class="panel">
      <span class="heading">Services Provided</span>
      <ul class="services">
        <li>Additions</li><li>Flooring</li>
        <li>Kitchens</li><li>Bathrooms</li>
        <li>Basements</li><li>Siding</li>
        <li>Windows</li><li>Doors</li>
        <li>Decks</li><li>Painting</li>
        <li>Roofing</li><li>Trim Work</li>
        <li>Attics</li><li>Design</li>
      </ul>
      <div class="tools" role="img" aria-label="Hard hat and tools on building plans"></div>
    </div>
  </div>
  <div class="inside-bottom">
    <div class="start">
      <h3>Getting Started is easy.</h3>
      <h2>GET EXCITED!</h2>
      <div class="steps">
        <div class="step"><b>1</b>Call us for a free estimate and tell us about your project.</div>
        <div class="step"><b>2</b>We visit, measure and share design ideas with you.</div>
        <div class="step"><b>3</b>Approve your plan and watch your new space come alive.</div>
      </div>
      <div class="photo" role="img" aria-label="Hard hat and blueprints"></div>
    </div>
    <div class="closing">
      <p>Thank you for considering Brightwater Home Renovations. We look forward to helping you create a home you love.</p>
      <p><b>Call 631-555-0148 today!</b></p>
      <div class="brand"><span class="brand-mark"></span><span class="brand-name">Brightwater</span></div>
    </div>
  </div>
</section>

</body>
</html>
```